Looking for an ecommerce website that specifically sells 1 product (Rapid Blue Comet Prime).... We do not need any shopping cart as we will be linking to our Corvana listing for purchasing.... similar to how this site does it:
http://www.plomaxen.com/
I want the following pages:
Home
Order
FAQ- we can take the copy from this site: http://quickbluecomet.com/
Contact us: just a basic contact form that will forward emails to contact@rbcprime-mail.com
Here is the layout design I want to copy:
http://www.plomaxen.com/
Of course we will use different colors to match this specific theme from the blue comet box, Black and Red
I also want to incorporate a design element from this site:
https://www.balduran.com/
As you can see, as you scroll down the page to read the copy, there is a left side panel that has the image of the product and the buying options available and a buy now for each one⦠please do the same on this new site..
Buying options:
FREE SHIPPING ON ALL ORDERS!
Preferred Package: Buy 5 get 1 free- 224.75
Power Package: 3 boxes (30 capsules)- 129.99
Intro Package: 1 box 10 capsules- $44.95
For copy for the site, we can get it from here:
http://quickbluecomet.com/
Some catch phrases to use:
100% Money Back Guarantee
QLB Certified Laboratory
100% All Natural Ingredients
Fast Acting
IMPORTANT- DO NOT USE ANY OF THE COPY THAT IS RELATED TO DEER ANTLER AS WE HAVE REMOVED THIS INGREDIENT FROM THE PRODUCT
I have attached images of the actual product here as well

```html
<!DOCTYPE html>
<html lang="en">
<head>
<meta charset="utf-8">
<title>Blue Comet Extreme</title>
<link href="https://fonts.googleapis.com/css2?family=Montserrat:wght@400;500;600;700;800&family=Open+Sans:wght@400;600;700&display=swap" rel="stylesheet">
<style>
  :root{
    --red:#c4061f;
    --red-dark:#9c1222;
    --grey:#5e5f63;
    --ink:#2b2b2e;
    --text:#3d3d40;
    --panel:#dcdce3;
    --panel-row:#e7e7ed;
    --panel-head:#5b5b5f;
    --white:#ffffff;
  }
  *{box-sizing:border-box;margin:0;padding:0}
  html,body{width:690px;height:1200px;overflow:hidden;background:var(--white)}
  body{position:relative;font-family:"Open Sans",Arial,sans-serif;color:var(--text)}
  .page{position:relative;width:690px;height:1200px;overflow:hidden}

  .hero-bg,.footer-bg{position:absolute;left:0;width:690px}
  .hero-bg{top:0;height:370px}
  .footer-bg{top:1090px;height:110px}

  .brand{position:absolute;left:72px;top:22px;font-family:"Montserrat",Arial,sans-serif;font-weight:800;font-size:17px;line-height:1;color:var(--red);letter-spacing:.5px;display:flex;align-items:center;gap:6px}
  .brand-dot{width:12px;height:12px;border-radius:50%;background:var(--red)}

  .main-nav{position:absolute;top:18px;left:318px;display:flex;gap:23px;font-family:"Montserrat",Arial,sans-serif;font-size:10.5px;font-weight:500;color:var(--ink)}
  .main-nav .active{color:var(--red)}

  .hero-title{position:absolute;left:63px;top:126px;font-family:"Montserrat",Arial,sans-serif;font-weight:700;font-size:20.5px;line-height:23px;color:var(--white);text-transform:uppercase}

  .badges{position:absolute;left:59px;top:206px;display:grid;grid-template-columns:148px 148px;gap:6px 4px}
  .badge{height:33px;background:rgba(60,40,45,.55);border:1px solid rgba(255,255,255,.35);display:flex;align-items:center;gap:8px;padding:0 8px;color:var(--white);font-family:"Montserrat",Arial,sans-serif;font-weight:600;font-size:7.6px;line-height:9.5px;text-transform:uppercase}
  .badge svg{flex:0 0 auto}

  .hero-product{position:absolute;left:390px;top:114px;width:220px;height:216px}
  .hero-product .back{position:absolute;left:0;top:22px;width:80px;height:164px;background:linear-gradient(90deg,#111,#2a2a2a);}
  .hero-product .front{position:absolute;left:68px;top:0;width:152px;height:216px;background:linear-gradient(160deg,#1a1a1a 0%,#0c0c0c 60%,#3a0a10 100%);box-shadow:0 6px 14px rgba(0,0,0,.35)}

  .sidebar{position:absolute;left:67px;top:384px;width:178px;height:668px;background:var(--panel)}
  .sidebar-head{height:50px;background:var(--panel-head);text-align:center;color:var(--white);font-family:"Montserrat",Arial,sans-serif;padding-top:15px}
  .sidebar-head strong{display:block;font-size:13.5px;font-weight:700;line-height:15px}
  .sidebar-head span{display:block;font-size:9px;font-weight:600;line-height:12px;text-transform:uppercase}
  .feature{position:relative;height:120px}
  .feature .pack{position:absolute;left:19px;top:60px}
  .pack{background:linear-gradient(160deg,#1c1c1c,#0b0b0b 65%,#3a0a10);box-shadow:2px 3px 5px rgba(0,0,0,.3)}
  .feature .pack{width:66px;height:90px;top:60px}
  .feature-copy{position:absolute;left:98px;top:64px;font-family:"Montserrat",Arial,sans-serif;font-weight:700;font-size:7.8px;line-height:12.8px;color:var(--ink);text-transform:uppercase}
  .btn{display:inline-block;background:var(--red);color:var(--white);font-family:"Montserrat",Arial,sans-serif;font-weight:700;text-transform:uppercase;text-align:center}
  .feature .btn{position:absolute;left:98px;top:123px;width:65px;height:20px;line-height:20px;font-size:8px}
  .select-title{position:absolute;left:14px;top:174px;font-family:"Montserrat",Arial,sans-serif;font-weight:500;font-size:9px;color:var(--ink);text-transform:uppercase}
  .package{position:absolute;left:14px;width:160px;height:47px;background:var(--panel-row)}
  .package .pack{position:absolute;left:12px;top:4px;width:31px;height:40px}
  .package .name{position:absolute;left:59px;top:8px;font-family:"Montserrat",Arial,sans-serif;font-weight:500;font-size:6.6px;line-height:7.8px;color:var(--ink);text-transform:uppercase}
  .package .price{position:absolute;left:59px;font-family:"Montserrat",Arial,sans-serif;font-weight:500;font-size:10.5px;color:var(--red)}
  .package .check{position:absolute;left:150px;width:9px;height:9px;background:var(--white);border:1px solid #888}
  .package .sel{position:absolute;left:144px;font-size:5px;font-weight:600;color:var(--ink)}
  .package .btn{position:absolute;left:120px;width:43px;height:12px;line-height:12px;font-size:6.5px}
  .shipping{position:absolute;left:10px;top:373px;width:159px;height:40px;background:linear-gradient(180deg,#d0101f,#a8111e);display:flex;align-items:center;gap:10px;padding-left:16px;color:var(--white);font-family:"Montserrat",Arial,sans-serif;font-weight:700;text-transform:uppercase}
  .shipping p{font-size:9.5px;line-height:11px}
  .shipping p span{font-size:11.5px}

  .content{position:absolute;left:270px;top:388px;width:350px}
  .content h1{font-family:"Montserrat",Arial,sans-serif;font-weight:400;font-size:16px;line-height:23px;color:var(--ink)}
  .content .lead{margin-top:7px;font-family:"Montserrat",Arial,sans-serif;font-weight:600;font-size:9.2px;color:var(--ink)}
  .content .hook{margin-top:9px;font-family:"Montserrat",Arial,sans-serif;font-weight:600;font-size:10px;color:var(--ink)}
  .content .intro{margin-top:9px;font-size:8.6px;line-height:13.6px}
  .benefits{margin-top:16px;list-style:none}
  .benefits li{position:relative;padding-left:10px;font-size:7.6px;line-height:10.4px;min-height:28px}
  .benefits li:last-child{min-height:0}
  .benefits li::before{content:"";position:absolute;left:0;top:2.5px;border-left:4px solid var(--red);border-top:3px solid transparent;border-bottom:3px solid transparent}
  .content h2{margin-top:30px;font-family:"Montserrat",Arial,sans-serif;font-weight:600;font-size:10px;line-height:15px;color:var(--ink)}
  .story{margin-top:8px;font-size:7.6px;line-height:10.4px}
  .story p{margin-bottom:7.2px}
  .story .gap{margin-top:16px}

  .footer-nav{position:absolute;left:75px;top:1140px;display:flex;gap:24px;font-family:"Montserrat",Arial,sans-serif;font-weight:500;font-size:9.5px;color:var(--white)}
  .copyright{position:absolute;left:75px;top:1160px;font-size:7px;color:var(--white)}
  .social{position:absolute;left:520px;top:1147px;display:flex;gap:5px}
  .social span{width:21px;height:21px;border:1.3px solid var(--white);border-radius:50%}
</style>
</head>
<body>
<div class="page">

  <svg class="hero-bg" viewBox="0 0 690 370" aria-hidden="true">
    <defs>
      <linearGradient id="heroGrad" x1="0" x2="1" y1="0" y2="0">
        <stop offset="0" stop-color="#5e5f63"/>
        <stop offset=".55" stop-color="#8a2a33"/>
        <stop offset="1" stop-color="#c4061f"/>
      </linearGradient>
    </defs>
    <path d="M0 48 H690 V300 C640 292 600 300 560 306 L560 306 C520 312 470 310 430 318 C330 338 180 350 0 330 Z" fill="#e8a3ac"/>
    <path d="M0 48 H690 V292 C600 285 540 300 470 316 C370 340 190 362 0 336 Z" fill="url(#heroGrad)"/>
    <path d="M0 0 H690 V48 H238 C226 48 224 76 200 76 H0 Z" fill="#ffffff"/>
  </svg>

  <div class="brand"><span>BLUE COMET EXTREME</span><span class="brand-dot"></span></div>

  <nav class="main-nav">
    <span class="active">HOME</span><span>PRODUCTS</span><span>ORDER</span><span>FAQ</span><span>CONTACT US</span>
  </nav>

  <h2 class="hero-title">Turbocharged male<br>sexual performance<br>within minutes!</h2>

  <div class="badges">
    <div class="badge">
      <svg width="22" height="22" viewBox="0 0 22 22" fill="none" stroke="#fff" stroke-width="1.3"><circle cx="11" cy="11" r="8.5" stroke-dasharray="3 2"/><text x="11" y="15" text-anchor="middle" font-size="11" fill="#fff" stroke="none" font-family="Arial">$</text></svg>
      <span>100% Money back<br>guarantee</span>
    </div>
    <div class="badge">
      <svg width="20" height="20" viewBox="0 0 20 20" fill="#fff"><path d="M10 18 V8 M10 12 C6 12 4 9 4 6 C7 6 10 8 10 12 Z M10 10 C14 10 16 7 16 4 C13 4 10 6 10 10 Z" stroke="#fff" stroke-width="1.2"/></svg>
      <span>100% All natural<br>ingredients</span>
    </div>
    <div class="badge">
      <svg width="20" height="20" viewBox="0 0 20 20" fill="none" stroke="#fff" stroke-width="1.5"><rect x="2" y="3" width="14" height="14" rx="1"/><path d="M5 10 L9 14 L18 3"/></svg>
      <span>QLB Certified<br>laboratory</span>
    </div>
    <div class="badge">
      <svg width="24" height="16" viewBox="0 0 24 16" fill="#fff"><path d="M2 14 A10 10 0 0 1 22 14 Z" opacity=".95"/><path d="M12 14 L17 6" stroke="#5e4a50" stroke-width="2"/></svg>
      <span>Fast acting</span>
    </div>
  </div>

  <div class="hero-product" role="img" aria-label="Black and red product box of Blue Comet Extreme with a heart emblem">
    <div class="back"></div>
    <div class="front"></div>
  </div>

  <aside class="sidebar">
    <div class="sidebar-head">
      <strong>BREAKTHROUGH!</strong>
      <span>Ancient medical discovery</span>
    </div>
    <div class="pack" style="position:absolute;left:19px;top:60px;width:66px;height:90px" role="img" aria-label="Product box"></div>
    <p class="feature-copy" style="position:absolute;left:98px;top:64px">No prescription<br>needed,<br>works fasts<br>lasts long!</p>
    <span class="btn" style="position:absolute;left:98px;top:123px;width:65px;height:20px;line-height:20px;font-size:8px">Buy now</span>

    <p class="select-title">Select your order</p>

    <div class="package" style="top:194px">
      <div class="pack" role="img" aria-label="Product box"></div>
      <p class="name">Preferred package:<br>buy 5 get 1 free</p>
      <p class="price" style="top:24px">$ 224.75</p>
      <span class="check" style="top:9px"></span><span class="sel" style="top:22px">SELECT</span>
      <span class="btn" style="top:30px">Submit</span>
    </div>
    <div class="package" style="top:252px">
      <div class="pack" role="img" aria-label="Product box"></div>
      <p class="name">Power package<br>3 boxes (30 capsules)</p>
      <p class="price" style="top:24px">$ 129.99</p>
      <span class="check" style="top:9px"></span><span class="sel" style="top:22px">SELECT</span>
      <span class="btn" style="top:30px">Submit</span>
    </div>
    <div class="package" style="top:311px">
      <div class="pack" role="img" aria-label="Product box"></div>
      <p class="name">Intro package<br>1 box 10 capsules</p>
      <p class="price" style="top:24px">$44.95</p>
      <span class="check" style="top:9px"></span><span class="sel" style="top:22px">SELECT</span>
      <span class="btn" style="top:30px">Submit</span>
    </div>

    <div class="shipping">
      <svg width="26" height="18" viewBox="0 0 26 18" fill="#fff"><rect x="0" y="2" width="15" height="10"/><path d="M16 5 H21 L25 9 V12 H16 Z"/><circle cx="5" cy="14" r="3" stroke="#b5101e" stroke-width="1.2"/><circle cx="20" cy="14" r="3" stroke="#b5101e" stroke-width="1.2"/></svg>
      <p>Free shipping on<br><span>all orders!</span></p>
    </div>
  </aside>

  <main class="content">
    <h1>Sounds too good to be true?<br>Maybe. I wouldn't argue with that.</h1>
    <p class="lead">But what I do know is...</p>
    <p class="hook">Virility, Stamina, And A Lava-hot Love Life Is Right Within Your Grasp!</p>
    <p class="intro">Can Blue Comet really change the way you think, perform and feel about sex?<br>It's hard not to be skeptical when you discover the potential benefits of Blue Comet:<br>Sends Your Sex Life Surging Into New Heights Of Intensity!</p>
    <ul class="benefits">
      <li>Blue Comet kicks your libido into overdrive within minutes! (No form of external stimulation. You don't even have to think 'dirty' for it to work. )</li>
      <li>Blue Comet energizes you so that you can go on like a raging bull without the need for taking a break.</li>
      <li>Blue Comete pumps so much fresh 'juice' into your erections, desire and performance, you'll be wondering where that extra 'inch' came from.</li>
      <li>Blue Comet gives you solid steel erections, and doesn't let up. You'll perform like a stud, in spite of yourself.</li>
      <li>Blue Comet desensitizes your penis so that any form of premature ejaculation becomes a thing of the past. You'll be able to give your partner hours of endless, non-stop pleasure.</li>
      <li>Blue Comet keeps you hard as a rock, even after multiple ejaculations! (Go ahead and erase the word 'limp' from your dictionary)</li>
      <li>Blue Comet stays in your body for up to 4 days. If you need to have sex repeatedly (and you'll probably want to), you will be able to do so with absolute ease!</li>
      <li style="min-height:18px">Blue Comet gives you all the OOMPH without any nasty side effects.</li>
      <li>Blue Comet eliminates 'performance anxiety' in men!</li>
    </ul>
    <h2>For hundreds of years, men around the world have relied on natural herbal remedies to help them maintain their vigor and virility.</h2>
    <div class="story">
      <p>he 100% natural herbal blend for Blue Comet was formulated with 3 core objectives in mind.</p>
      <p>Objective #1: To help increase "Chi" or life force energy.</p>
      <p>Objective #2: To channel maximum blood flow to the penis.</p>
      <p>Objective #3: To skyrocket your libido</p>
      <p class="gap">All 3 objectives had to be achieved concurrently.</p>
      <p>Obviously you already know about the 'mighty' ant and it's incredible aphrodisiac properties.</p>
      <p>But what you may not know is that the 'ant tonics' used by the ancient Chinese imperial emperors, were used to increase their Yang Jing, or 'Chi'.</p>
      <p>You see, the Chinese believe that ejaculation of the male seed for purposes other than having children is a wasteful loss of an extremely precious treasure.</p>
      <p>The energy loss over long periods of time weakens the physical health of the male.</p>
      <p>You may or may not buy this 'theory', but it may make sense to you when you realize that if ALL of your sperm that you ejaculated was fertilized, then you could have produced the equivalent of a COUNTRY'S population.</p>
      <p>Think about how much 'energy' is needed to engineer such a phenomenon.</p>
    </div>
  </main>

  <svg class="footer-bg" viewBox="0 0 690 110" aria-hidden="true">
    <defs>
      <linearGradient id="footGrad" x1="0" x2="1" y1="0" y2="0">
        <stop offset="0" stop-color="#5e5f63"/>
        <stop offset=".55" stop-color="#8a2a33"/>
        <stop offset="1" stop-color="#c4061f"/>
      </linearGradient>
    </defs>
    <path d="M0 22 C150 0 260 6 380 14 C500 22 600 12 690 2 V110 H0 Z" fill="url(#footGrad)"/>
  </svg>

  <nav class="footer-nav"><span>HOME</span><span>PRODUCTS</span><span>ORDER</span><span>FAQ</span><span>CONTACT US</span></nav>
  <p class="copyright">© 2018 Company Name&nbsp; All right reserved</p>
  <div class="social" aria-label="Social links"><span></span><span></span><span></span><span></span></div>

</div>
</body>
</html>
```